Web Design Project for an operational risk management consulting company

Website is for a consulting company specialising in operational risk management. Our specialist areas include crisis and emergency management, community engagement, safety and security. We work internationally, generally in high hazard environments. We are a highly ethical and professional company which prides itself on delivering a strong level of customer service.

As a company we recognise that the key to keeping people safe is ensuring that they work in an ethical and sustainable manner. Therefore we are as much about soft skills as we are about hard skills. We would like our website and supporting images to reflect this.
We have worked throughout Africa and the Middle east, as well as Asia pacific. An international flavour to the website would also be great.
Background images on www.corvellpartnersglobal.example are a good example of what we are thinking of, though very open to fresh ideas.

Target Market(s)

Our customers are generally medium to large organisations who work internationally. We would like to also support more not for profits and non government organisations who work in hazardous environments

Industry/Entity Type

It Company

Number of Pages Required

5+ page

Font styles to use
Sans Serif

Requirements
Must have
• Easy to edit by non IT people
• Section for blogs/news updates
• Pages should include:
• (A) home page
• (B) about us
• (C) services
• (D) contact
• (E) insights
Nice to have
• An international and professional theme. Some gritty images that symbolise the risks associated with working in unstable environments, as well as some human ones and that of the environment
Should not have
• Cartoonish or generic images
• Not focus on traditional physical security aspects

```html
<!DOCTYPE html>
<html lang="en">
<head>
<meta charset="utf-8">
<title>Kestrel Risk</title>
<link href="https://fonts.googleapis.com/css2?family=Open+Sans:ital,wght@0,400;0,600;0,700;0,800;1,400;1,600&display=swap" rel="stylesheet">
<style>
:root{
  --navy:#0b3552;
  --blue:#0f4f7c;
  --accent:#1b6fa8;
  --ink:#2b2f33;
  --muted:#6c737a;
  --light:#eef0f2;
  --card:#e6e8ea;
  --dark:#1f2326;
  --darker:#15181a;
  --white:#ffffff;
}
*{box-sizing:border-box;margin:0;padding:0}
html,body{width:1200px;height:2836px;overflow:hidden}
body{font-family:"Open Sans",Arial,sans-serif;color:var(--ink);background:var(--white);position:relative}
section,header,footer{position:absolute;left:0;width:1200px}

/* hero */
.hero{top:0;height:680px;background:linear-gradient(180deg,#4a5660 0%,#6f7a83 35%,#3b4650 70%,#232b31 100%);color:var(--white)}
.hero-photo{position:absolute;inset:0;background:radial-gradient(ellipse at 50% 30%,rgba(200,210,220,.35),transparent 60%),linear-gradient(180deg,rgba(20,40,60,.15),rgba(10,20,30,.55))}
.brand{position:absolute;left:0;top:0;width:280px;height:150px;background:var(--white);clip-path:polygon(0 0,100% 0,84% 100%,0 100%);display:flex;align-items:center;padding-left:30px;gap:12px;white-space:nowrap}
.brand-mark{width:40px;height:40px;border-radius:50%;background:var(--blue);flex:none}
.brand-name{font-size:26px;font-weight:700;color:var(--blue)}
.topbar{position:absolute;right:0;top:0;width:950px;height:150px;background:linear-gradient(90deg,rgba(11,53,82,0) 0%,rgba(11,53,82,.85) 45%,var(--navy) 100%)}
.social-top{position:absolute;right:70px;top:46px;display:flex;gap:8px}
.social-top span{width:24px;height:24px;border-radius:50%;background:var(--white);opacity:.9}
.nav{position:absolute;right:60px;top:100px;display:flex;height:40px;align-items:center}
.nav a{color:var(--white);text-decoration:none;font-size:13px;font-weight:600;padding:0 26px;letter-spacing:.5px;white-space:nowrap}
.nav a.active{background:var(--darker);height:40px;line-height:40px}
.hero-copy{position:absolute;top:370px;width:100%;text-align:center}
.hero-copy h1{font-size:40px;font-weight:800;letter-spacing:1px}
.hero-copy p{font-size:24px;margin-top:8px}
.btn-outline{display:inline-block;margin-top:26px;border:2px solid var(--white);padding:12px 26px;font-size:15px;font-weight:700;color:var(--white)}

/* about */
.about{top:680px;height:350px;text-align:center;padding-top:48px}
.about h2{font-size:30px;font-weight:700;color:var(--blue)}
.about .sub{font-size:13px;color:var(--accent);margin-top:6px}
.about .body{width:900px;margin:28px auto 0;font-size:12.5px;line-height:1.75;color:var(--muted)}
.about .body p+p{margin-top:18px}

/* work */
.work{top:1030px;height:370px;background:var(--blue);color:var(--white)}
.work h2{position:absolute;left:80px;top:44px;font-size:30px;font-weight:700}
.work-intro{position:absolute;left:80px;top:100px;width:300px;font-size:13px;line-height:1.8}
.work-more{position:absolute;left:80px;top:290px;font-size:13px;display:flex;align-items:center;gap:8px}
.work-more i{width:20px;height:20px;border-radius:50%;background:var(--white)}
.work-grid{position:absolute;left:500px;top:44px;display:grid;grid-template-columns:repeat(3,190px);column-gap:30px;row-gap:14px}
.work-thumb{height:96px;border:3px solid var(--white)}
.t1{background:linear-gradient(135deg,#dfe6ec,#9fb0be)}
.t2{background:linear-gradient(135deg,#c9d2db,#6f7f90)}
.t3{background:linear-gradient(135deg,#1e2a36,#3b4b5b)}
.t4{background:linear-gradient(135deg,#2a3644,#101820)}
.t5{background:linear-gradient(135deg,#e8ecef,#8d9aa6)}
.t6{background:linear-gradient(135deg,#d5dbe0,#5f6c78)}
.work-cap{font-size:11px;line-height:1.5;margin-top:7px}

/* blog & news */
.updates{top:1400px;height:560px;background:var(--light)}
.col{position:absolute;top:60px;width:520px}
.col.blog{left:72px}.col.news{left:620px}
.col h2{font-size:30px;font-weight:700;color:var(--blue);margin-bottom:24px}
.card{position:relative;background:var(--card);height:320px;padding:30px 50px 20px 28px}
.card h3{font-size:15px;font-weight:600;color:var(--accent);letter-spacing:1px;text-transform:uppercase}
.card .meta{font-size:12px;color:var(--muted);margin-top:4px;font-style:italic}
.card p{font-size:12px;line-height:1.8;color:var(--muted);margin-top:14px}
.card .next{position:absolute;right:0;top:120px;width:26px;height:60px;background:var(--navy)}
.news .card{padding-left:120px}
.ribbon{position:absolute;left:16px;top:-18px;width:76px;height:110px;background:var(--accent);color:var(--white);text-align:center;font-size:12px;font-weight:600;padding-top:26px;clip-path:polygon(0 0,100% 0,100% 100%,50% 84%,0 100%)}

/* testimonial */
.voices{top:1960px;height:460px;background:linear-gradient(180deg,#2a3035 0%,#3f464c 50%,#1e2327 100%);color:var(--white);text-align:center}
.voices h2{margin-top:56px;font-size:30px;font-weight:700}
.voices blockquote{width:960px;margin:34px auto 0;font-size:17px;font-style:italic;line-height:1.6}
.avatar{width:90px;height:90px;border-radius:50%;background:linear-gradient(135deg,#8a9198,#4b5258);border:4px solid var(--white);margin:42px auto 0}
.who{margin-top:18px;font-size:15px;font-style:italic}
.who b{font-weight:700;font-style:normal}

/* contact */
.contact{top:2420px;height:350px;background:var(--dark);color:var(--white);text-align:center}
.contact h2{margin-top:58px;font-size:26px;font-weight:700}
.social-row{display:flex;justify-content:center;gap:14px;margin-top:24px}
.social-row span{width:34px;height:34px;border:1px solid #9aa1a7;background:#2d3236}
.contact .note{font-size:12px;color:#b9bfc4;margin-top:20px}
.field{width:720px;height:40px;margin:16px auto 0;background:#3a3f43;border:1px solid #5a6065;text-align:left;padding:10px 14px;font-size:12px;color:#9aa1a7}
.btn-submit{display:inline-block;margin-top:20px;border:2px solid var(--white);padding:8px 24px;font-size:13px;font-weight:600}
.legal{top:2770px;height:66px;background:var(--darker);color:#9aa1a7;font-size:12px;text-align:center;line-height:66px}
</style>
</head>
<body>

<header class="hero">
  <div class="hero-photo" role="img" aria-label="Aerial view of a dense city skyline in muted blue-grey tones"></div>
  <div class="topbar">
    <div class="social-top"><span></span><span></span><span></span><span></span></div>
    <nav class="nav">
      <a class="active" href="#">HOME PAGE</a><a href="#">ABOUT US</a><a href="#">SERVICES</a><a href="#">CONTACT</a><a href="#">INSIGHTS</a>
    </nav>
  </div>
  <div class="brand"><span class="brand-mark"></span><span class="brand-name">Kestrel Risk</span></div>
  <div class="hero-copy">
    <h1>HOW PEOPLE KNOW YOU?</h1>
    <p>We, online Marketing &amp; Social Media Consultation is on the house</p>
    <span class="btn-outline">CLAIM FREE CONSULTATION</span>
  </div>
</header>

<section class="about">
  <h2>ABOUT KESTREL RISK</h2>
  <div class="sub">We Always Help Your Business Grow</div>
  <div class="body">
    <p>Lorem ipsum is simply dummy text of the printing and typesetting industry. Lorem ipsum has been the industry's standard dummy text ever since the 1500s, when an unknown printer took a galley of type and scrambled it to make a type specimen book. It has survived not only five centuries, but also the leap into electronic typesetting, remaining essentially unchanged. It was popularised in the 1960s with the release of Typeline sheets containing Lorem Ipsum passages, and more recently with desktop publishing software like Folio Layout including versions of Lorem Ipsum.</p>
    <p>Lorem ipsum is simply dummy text of the printing and typesetting industry. Lorem ipsum has been the industry's standard dummy text ever since the 1500s, when an unknown printer took a galley of type and scrambled it to make a type specimen book.</p>
  </div>
</section>

<section class="work">
  <h2>OUR WORK</h2>
  <p class="work-intro">Lorem ipsum is simply dummy text of the printing and typesetting industry. Lorem ipsum has been the industry's standard dummy text ever since the 1500s, when an unknown printer took a galley of type and scrambled it to make a type specimen book.</p>
  <div class="work-more">View More <i></i></div>
  <div class="work-grid">
    <div><div class="work-thumb t1" role="img" aria-label="Team meeting around a table"></div><p class="work-cap">Lorem ipsum is simply dummy text of the printing and type setting industry.</p></div>
    <div><div class="work-thumb t2" role="img" aria-label="Consultants shaking hands"></div><p class="work-cap">Lorem ipsum is simply dummy text of the printing and type setting industry.</p></div>
    <div><div class="work-thumb t3" role="img" aria-label="Dark abstract project image"></div><p class="work-cap">Lorem ipsum is simply dummy text of the printing and type setting industry.</p></div>
    <div><div class="work-thumb t4" role="img" aria-label="Dark abstract project image"></div><p class="work-cap">Lorem ipsum is simply dummy text of the printing and type setting industry.</p></div>
    <div><div class="work-thumb t5" role="img" aria-label="Colleagues reviewing documents"></div><p class="work-cap">Lorem ipsum is simply dummy text of the printing and type setting industry.</p></div>
    <div><div class="work-thumb t6" role="img" aria-label="Professional at a desk"></div><p class="work-cap">Lorem ipsum is simply dummy text of the printing and type setting industry.</p></div>
  </div>
</section>

<section class="updates">
  <div class="col blog">
    <h2>LATEST BLOG</h2>
    <article class="card">
      <h3>There are variations of 404 passages</h3>
      <div class="meta">By jackson, 24, 2016</div>
      <p>Sed ut perspiciatis unde omnis iste natus error sit voluptatem accusantium doloremque laudantium, totam rem aperiam, eaque ipsa quae ab illo inventore veritatis et quasi architecto beatae vitae dicta sunt explicabo. Nemo enim ipsam voluptatem quia voluptas sit aspernatur aut odit aut fugit, sed quia consequuntur magni dolores eos qui ratione voluptatem sequi nesciunt.</p>
      <span class="next"></span>
    </article>
  </div>
  <div class="col news">
    <h2>LATEST NEWS</h2>
    <article class="card">
      <div class="ribbon">24th<br>Jan<br>2016</div>
      <h3>But I must explain to how all</h3>
      <p>Sed ut perspiciatis unde omnis iste natus error sit voluptatem accusantium doloremque laudantium, totam rem aperiam, eaque ipsa quae ab illo inventore veritatis et quasi architecto beatae vitae dicta sunt explicabo. Nemo enim ipsam voluptatem quia voluptas sit aspernatur.</p>
      <span class="next"></span>
    </article>
  </div>
</section>

<section class="voices">
  <h2>WHAT PEOPLE SAY</h2>
  <blockquote>"Lorem ipsum dolor sit amet, consectetur adipiscing elit. Morbi hendrerit elit turpis, a porttitor tellus sollicitudin at. Class aptent taciti sociosqu ad litora torquent per conubia nostra, per inceptos himenaeos."</blockquote>
  <div class="avatar" role="img" aria-label="Portrait of the client giving the testimonial"></div>
  <div class="who"><b>MARA ELLSWORTH</b> Fitness Enthusiast, NORTHGATE</div>
</section>

<section class="contact">
  <h2>Get in touch</h2>
  <div class="social-row"><span></span><span></span><span></span><span></span></div>
  <p class="note">Subscribe to our newsletter to stay update with what is new</p>
  <div class="field">Email Address</div>
  <span class="btn-submit">Subscribe</span>
</section>

<footer class="legal">Copyright 2016 &copy; Kestrel Risk. All Right Reserved.</footer>

</body>
</html>
```